VMR business card

Need a business card for a company that provides instructional design and elearning development services. The website is here: http://vantmoro.studio/

I'm attaching a current logo, as well as the old business card design. While I like to keep it clean, the old design is too simplistic for my liking. The only idea I want to reuse from the old design is placing industry jargon on the back of the card, just need a better way to present it. But if you have other ideas for the back--feel free to experiment.

Please use the colors complementary to the color we have on the website. Thank you!

```html
<!DOCTYPE html>
<html lang="en">
<head>
<meta charset="utf-8">
<title>VMR business card</title>
<link rel="stylesheet" href="https://fonts.googleapis.com/css2?family=Open+Sans:wght@400;600;700;800&display=swap">
<style>
  :root {
    --stage: #2b2b2b;
    --teal: #1fae94;
    --teal-light: #3cc7ab;
    --teal-dark: #138a74;
    --ink: #0b0b0b;
    --paper: #ffffff;
    --paper-shade: #e4e4e4;
    --label: #1c1c1c;
    --muted: #555555;
    --photo-light: #eeeeee;
    --photo-mid: #c9cdd0;
    --photo-dark: #9aa2a8;
  }
  html, body {
    margin: 0;
    width: 1200px;
    height: 997px;
    overflow: hidden;
    background: var(--stage);
    font-family: "Open Sans", Arial, sans-serif;
  }
  .card {
    position: absolute;
    width: 740px;
    height: 420px;
    border-radius: 18px;
    box-shadow: 0 14px 30px rgba(0,0,0,.55);
  }
  .card-front { left: 180px; top: 50px; }
  .card-back  { left: 280px; top: 522px; }
  .card svg { display: block; width: 740px; height: 420px; }
  .brand { font-weight: 800; fill: var(--teal); }
  .tagline { font-weight: 600; fill: var(--muted); font-size: 15px; }
  .person-name { font-weight: 700; fill: var(--teal); font-size: 21px; }
  .person-role { font-weight: 400; fill: var(--paper); font-size: 15px; }
  .contact { font-weight: 400; fill: var(--teal-light); font-size: 16px; }
  .service-label { font-weight: 800; fill: var(--label); font-size: 13px; letter-spacing: .5px; }
  .visit { font-weight: 600; fill: var(--teal-light); font-size: 19px; }
  .site { font-weight: 600; fill: var(--paper); font-size: 18px; }
</style>
</head>
<body>

<!-- Front of card -->
<div class="card card-front">
  <svg viewBox="0 0 740 420" xmlns="http://www.w3.org/2000/svg">
    <defs>
      <clipPath id="front-shape"><rect width="740" height="420" rx="18"/></clipPath>
      <linearGradient id="front-paper" x1="0" y1="0" x2="0" y2="1">
        <stop offset="0" stop-color="var(--paper)"/>
        <stop offset="1" stop-color="var(--paper-shade)"/>
      </linearGradient>
    </defs>
    <g clip-path="url(#front-shape)">
      <rect width="740" height="420" fill="url(#front-paper)"/>
      <path class="wave-teal" d="M0,262 C250,318 470,196 740,150 L740,420 L0,420Z" fill="var(--teal)"/>
      <path class="wave-teal-light" d="M0,278 C250,334 480,212 740,172 L740,420 L0,420Z" fill="var(--teal-light)"/>
      <path class="wave-ink" d="M0,294 C255,352 490,228 740,194 L740,420 L0,420Z" fill="var(--ink)"/>

      <text class="brand" x="370" y="168" font-size="76" text-anchor="middle">VMR</text>
      <text class="tagline" x="370" y="198" text-anchor="middle">Ready to take your learning on the go?</text>

      <text class="person-name" x="38" y="332">Dorian Kelwick</text>
      <text class="person-role" x="38" y="354">Owner</text>

      <g class="icon-phone" transform="translate(38,368)" fill="var(--paper)">
        <path d="M1,4 Q8,-1 15,4 L13,7 Q8,4 3,7Z"/>
        <rect x="3" y="8" width="10" height="6" rx="1"/>
      </g>
      <text class="contact" x="64" y="382">555-014-2837</text>

      <g class="icon-mail" transform="translate(38,394)">
        <rect width="16" height="11" rx="1" fill="var(--paper)"/>
        <path d="M0,0 L8,6 L16,0" fill="none" stroke="var(--ink)" stroke-width="1.5"/>
      </g>
      <text class="contact" x="64" y="405">dkelwick@vantmoro.studio</text>
    </g>
  </svg>
</div>

<!-- Back of card -->
<div class="card card-back">
  <svg viewBox="0 0 740 420" xmlns="http://www.w3.org/2000/svg">
    <defs>
      <clipPath id="back-shape"><rect width="740" height="420" rx="18"/></clipPath>
      <linearGradient id="photo-wash" x1="0" y1="0" x2="1" y2="1">
        <stop offset="0" stop-color="var(--photo-light)"/>
        <stop offset=".6" stop-color="var(--photo-mid)"/>
        <stop offset="1" stop-color="var(--photo-dark)"/>
      </linearGradient>
    </defs>
    <g clip-path="url(#back-shape)">
      <rect class="photo-backdrop" width="740" height="420" fill="url(#photo-wash)" role="img" aria-label="Faded photo of a businessman in shirt and tie"/>

      <g class="photo-tiles" role="img" aria-label="Hexagon tiles with photos of learning, charts and handshake scenes" fill="#b3b9bd" stroke="var(--photo-light)" stroke-width="4">
        <polygon points="60,190 90,140 150,140 180,190 150,240 90,240"/>
        <polygon points="180,120 210,70 270,70 300,120 270,170 210,170"/>
        <polygon points="180,230 205,190 255,190 280,230 255,270 205,270" fill="#a4abb0"/>
        <polygon points="300,150 335,95 405,95 440,150 405,205 335,205" fill="#c2c7ca"/>
        <polygon points="450,100 475,60 525,60 550,100 525,140 475,140" fill="#bfc5c9"/>
      </g>

      <text class="brand" x="130" y="95" font-size="48">VMR</text>

      <path d="M0,318 C210,345 430,255 740,140 L740,420 L0,420Z" fill="var(--teal-dark)"/>
      <path d="M0,334 C215,360 440,270 740,158 L740,420 L0,420Z" fill="var(--teal)"/>
      <path d="M0,360 C220,388 460,300 740,188 L740,420 L0,420Z" fill="var(--ink)"/>

      <text class="visit" x="710" y="300" text-anchor="end">Visit us on</text>
      <text class="site" x="710" y="328" text-anchor="end">www.vantmoro.studio</text>

      <g class="service">
        <text class="service-label" x="150" y="262" text-anchor="middle">INSTRUCTIONAL</text>
        <text class="service-label" x="150" y="278" text-anchor="middle">DESIGN</text>
        <circle cx="150" cy="335" r="38" fill="var(--teal)" stroke="var(--paper-shade)" stroke-width="5"/>
        <path d="M138,324 h8 a4,4 0 1 1 8,0 h8 v8 a4,4 0 1 0 0,8 v8 h-24Z" fill="var(--paper)"/>
      </g>
      <g class="service">
        <text class="service-label" x="305" y="220" text-anchor="middle">E-LEARNING</text>
        <text class="service-label" x="305" y="236" text-anchor="middle">DEVELOPMENT</text>
        <circle cx="305" cy="292" r="38" fill="var(--teal)" stroke="var(--paper-shade)" stroke-width="5"/>
        <rect x="290" y="282" width="22" height="18" rx="3" fill="var(--paper)"/>
        <path d="M312,286 a5,5 0 0 1 0,10" fill="none" stroke="var(--paper)" stroke-width="3"/>
        <rect x="286" y="302" width="32" height="3" rx="1.5" fill="var(--paper)"/>
      </g>
      <g class="service">
        <text class="service-label" x="460" y="160" text-anchor="middle">MOBILE</text>
        <text class="service-label" x="460" y="176" text-anchor="middle">LEARNING</text>
        <circle cx="460" cy="232" r="38" fill="var(--teal)" stroke="var(--paper-shade)" stroke-width="5"/>
        <path d="M444,244 a9,9 0 0 1 2,-17 a12,12 0 0 1 23,-2 a9,9 0 0 1 4,19Z" fill="var(--paper)"/>
        <path d="M460,240 v-12 m-6,5 l6,-6 l6,6" fill="none" stroke="var(--teal)" stroke-width="3"/>
      </g>
      <g class="service">
        <text class="service-label" x="630" y="70" text-anchor="middle">INSTRUCTOR-LED</text>
        <text class="service-label" x="630" y="86" text-anchor="middle">TRAINING</text>
        <circle cx="630" cy="160" r="38" fill="var(--teal)" stroke="var(--paper-shade)" stroke-width="5"/>
        <rect x="614" y="150" width="32" height="22" rx="3" fill="var(--paper)"/>
        <rect x="623" y="145" width="14" height="6" rx="2" fill="var(--paper)"/>
        <circle cx="630" cy="161" r="6" fill="var(--teal)"/>
      </g>
    </g>
  </svg>
</div>

</body>
</html>
```